Halbrook Masonry- Business Card Design

We need a business card design for a new company based in Canberra ACT. We build Rock Retaining Walls, commercial and domestic.
We would like to see designs that use HM letters combine as logo and use stone sandstone or blue rocks. Final design of the business card should communicate strong, wealthy, Rock retaining walls

Target Market(s)

Everybody who needs stone retaining wall in there backyard

Industry/Entity Type

Business

Contact Information for Business Card

HM
Halbrook Masonry,
Dario Veltek (Stonemason)
Phone/ 0498 317 245
PO Box 3958 Kenley ACT 2609
E-mail/dveltek@tarnimail.net.au
www.halbrookmasonry.com.au

Requirements
Must have
• Letters HM combine as logo. "HALBROOK MASONRY" as features
Nice to have
• Rock: Sandstone or bluestone

```html
<!DOCTYPE html>
<html lang="en">
<head>
<meta charset="utf-8">
<title>Halbrook Masonry – Business Card</title>
<link rel="stylesheet" href="https://fonts.googleapis.com/css2?family=Caladea:ital,wght@0,400;0,700;1,400&display=swap">
<style>
  :root {
    --backdrop: #3a3a3a;
    --card-black: #161616;
    --card-black-light: #262626;
    --card-red: #b81f26;
    --text-white: #f4f1ec;
    --text-soft: #e6c4c2;
    --stone: #cfc2a3;
  }
  * { margin: 0; padding: 0; box-sizing: border-box; }
  html, body {
    width: 1200px;
    height: 949px;
    overflow: hidden;
    background: var(--backdrop);
  }
  .business-card {
    position: absolute;
    left: 100px;
    top: 195px;
    width: 1000px;
    height: 560px;
    display: flex;
    font-family: "Caladea", Georgia, serif;
  }
  .card-brand {
    position: relative;
    width: 640px;
    height: 100%;
    background: radial-gradient(ellipse at 40% 35%, var(--card-black-light), var(--card-black) 70%);
    color: var(--text-white);
  }
  .brand-mark {
    position: absolute;
    left: 0;
    right: 0;
    top: 120px;
    display: flex;
    justify-content: center;
    align-items: center;
    gap: 18px;
  }
  .brand-mark-square {
    width: 34px;
    height: 34px;
    background: var(--stone);
  }
  .brand-mark-name {
    font-size: 84px;
    font-weight: 700;
    color: var(--stone);
    line-height: 1;
  }
  .company-name {
    position: absolute;
    left: 0;
    right: 0;
    top: 300px;
    text-align: center;
    font-size: 40px;
    font-weight: 700;
    letter-spacing: 1px;
  }
  .company-address {
    position: absolute;
    left: 0;
    right: 0;
    top: 352px;
    text-align: center;
    font-size: 27px;
  }
  .card-contact {
    position: relative;
    width: 360px;
    height: 100%;
    background: var(--card-red);
    text-align: right;
    padding: 36px 34px 0 0;
  }
  .person-name {
    font-size: 42px;
    color: var(--text-soft);
    line-height: 1.1;
  }
  .person-role {
    font-size: 34px;
    font-style: italic;
    color: var(--text-white);
    line-height: 1.1;
  }
  .person-phone {
    font-size: 36px;
    color: var(--text-soft);
    line-height: 1.1;
  }
  .person-email {
    font-size: 22px;
    color: var(--text-soft);
    margin-top: 6px;
  }
  .company-web {
    position: absolute;
    right: 34px;
    bottom: 22px;
    font-size: 21px;
    color: var(--text-soft);
  }
</style>
</head>
<body>
  <div class="business-card">
    <section class="card-brand">
      <div class="brand-mark">
        <span class="brand-mark-square"></span>
        <span class="brand-mark-name">HM</span>
      </div>
      <h1 class="company-name">HALBROOK MASONRY</h1>
      <p class="company-address">PO Box 3958 Kenley ACT 2609</p>
    </section>
    <section class="card-contact">
      <p class="person-name">Dario Veltek</p>
      <p class="person-role">(Stonemason)</p>
      <p class="person-phone">0498 317 245</p>
      <p class="person-email">dveltek@tarnimail.net.au</p>
      <p class="company-web">www.halbrookmasonry.com.au</p>
    </section>
  </div>
</body>
</html>
```